Anchored Willow Website

Would like a website designed for my fitness and nutrition coaching company Anchor Willow. I have a company logo and would like to keep the page layout clean and simple. Needs to look great on computer and mobile devices.

Target Market(s)

Target market is individuals looking to make changes in their health and nutrition with the help of an online coach.

Industry/Entity Type

Fitness

Number of Pages Required

2 page

Colors
3176b5
0355a3
85acd3
cedeed
f8fcfd
ffffff

Requirements
Must have
• The first page should have the company logo and name towards the top and below that client before and after photos scrolling or displaying in some manner. Also would like a section that states services offered and a section about myself since I am the primary coach for clients.

```html
<!DOCTYPE html>
<html lang="en">
<head>
<meta charset="utf-8">
<title>Anchored Willow — Fitness &amp; Nutrition Coaching</title>
<link href="https://fonts.googleapis.com/css2?family=Montserrat:wght@400;500;600;700;800&family=Open+Sans:wght@400;600&display=swap" rel="stylesheet">
<style>
  :root{
    --blue:#0f6fc0;
    --blue-deep:#0355a3;
    --blue-mid:#3176b5;
    --blue-soft:#85acd3;
    --blue-pale:#cedeed;
    --mist:#e6edf5;
    --white:#ffffff;
    --nav-grey:#6d6e70;
    --panel-grey:#a3a3a5;
    --frame-grey:#55585c;
    --ink:#4a4a4c;
    --text:#5e6266;
  }
  *{margin:0;padding:0;box-sizing:border-box}
  html,body{width:1200px;height:2517px;overflow:hidden}
  body{position:relative;background:var(--white);font-family:"Open Sans",Arial,sans-serif;color:var(--text)}
  .abs{position:absolute}

  /* top bar */
  .topbar{left:0;top:0;width:1200px;height:44px;background:var(--nav-grey)}
  .topbar .social{left:24px;top:16px;display:flex;gap:8px}
  .dot{width:11px;height:11px;border-radius:50%;background:var(--white);display:block}
  .nav{position:absolute;top:0;left:0;width:1200px;height:44px}
  .nav a{position:absolute;top:0;height:44px;line-height:44px;font-family:"Montserrat",sans-serif;font-size:11px;font-weight:600;letter-spacing:2px;color:var(--white);text-decoration:none;transform:translateX(-50%);padding:0 14px;white-space:nowrap}
  .nav a.active{background:var(--blue)}
  .topbar .contact{right:26px;top:14px;display:flex;gap:12px}

  /* hero */
  .hero-photo{left:0;top:44px;width:600px;height:489px;background:linear-gradient(135deg,#c9ccd0 0%,#8a8f95 45%,#4b4f55 100%)}
  .hero-blue{left:600px;top:44px;width:600px;height:489px;background:linear-gradient(120deg,#2f7cc4 0%,#1f6cb5 55%,#2a77bf 100%)}
  .hero-word{top:276px;font-family:"Montserrat",sans-serif;font-weight:700;font-size:36px;color:var(--white);letter-spacing:1px}
  .hero-word .mark{display:inline-block;width:16px;height:16px;background:var(--white);transform:rotate(45deg);margin-left:14px;vertical-align:middle}
  .hero-fitness{left:233px}
  .hero-nutrition{left:856px}
  .hero-badge{left:458px;top:143px;width:284px;height:284px}
  .brand-hero{left:440px;top:276px;width:320px;text-align:center;font-family:"Montserrat",sans-serif;font-weight:600;font-size:18px;color:var(--blue);letter-spacing:.5px}
  .slider-dots{left:250px;top:507px;display:flex;gap:6px}
  .slider-dots span{width:6px;height:6px;border-radius:50%;background:var(--white);opacity:.85}
  .slider-dots span:first-child{background:var(--blue-soft)}
  .slider-dots.right{left:880px}
  .slider-dots.right span{background:var(--blue-soft);opacity:.5}

  /* welcome */
  .welcome{left:0;top:533px;width:1200px;height:577px;background:var(--mist)}
  .welcome-art{left:256px;top:624px;width:380px;height:460px}
  .welcome-title{left:730px;top:660px;font-family:"Montserrat",sans-serif;font-weight:700;font-size:38px;letter-spacing:.5px;color:var(--blue)}
  .welcome-title span{color:#5a5c60}
  .copy{font-size:11.5px;line-height:20.5px;color:var(--text)}
  .welcome-copy{left:734px;top:714px;width:380px}
  .welcome-copy p+p{margin-top:9px}

  /* call to action */
  .cta-left{left:0;top:1110px;width:583px;height:410px;background:linear-gradient(160deg,#1c4f86 0%,#123d6d 60%,#0d2f57 100%)}
  .cta-right{left:583px;top:1110px;width:617px;height:410px;background:linear-gradient(200deg,#2d78c0 0%,#1a62a8 50%,#134f8d 100%)}
  .cta-text{left:380px;top:1218px;width:440px;text-align:center;color:var(--white);font-family:"Montserrat",sans-serif}
  .cta-kicker{font-size:32px;font-weight:500;letter-spacing:10px;line-height:40px}
  .cta-main{font-size:68px;font-weight:700;letter-spacing:6px;line-height:68px}
  .cta-sub{font-size:29px;font-weight:500;letter-spacing:5px;line-height:38px}
  .cta-button{left:503px;top:1388px;width:215px;height:33px;background:var(--blue-pale);color:var(--blue);font-family:"Montserrat",sans-serif;font-weight:600;font-size:17px;letter-spacing:5px;text-align:center;line-height:33px}

  /* services */
  .section-title{font-family:"Montserrat",sans-serif;font-weight:600;color:var(--blue);letter-spacing:8px}
  .services-title{left:0;top:1560px;width:1200px;text-align:center;font-size:22px}
  .service{top:1680px;width:200px;margin-left:-100px;text-align:center}
  .service svg.icon{display:block;margin:0 auto;height:44px}
  .service h3{margin-top:30px;font-family:"Montserrat",sans-serif;font-weight:600;font-size:13px;letter-spacing:4px;color:var(--blue)}
  .service .tag{display:block;width:16px;height:16px;background:#707276;transform:rotate(45deg);margin:34px auto 0}

  /* before / after */
  .result-panel{left:0;top:1894px;width:583px;height:419px;background:var(--panel-grey)}
  .result-photo{left:583px;top:1894px;width:617px;height:419px;background:linear-gradient(110deg,#d9dcd6 0%,#8f7a66 40%,#b8c96a 60%,#e8e6e0 100%)}
  .result-kicker{left:74px;top:2015px;font-family:"Montserrat",sans-serif;font-weight:600;font-size:20px;letter-spacing:5px;color:var(--white)}
  .result-title{left:74px;top:2037px;font-family:"Montserrat",sans-serif;font-weight:600;font-size:34px;letter-spacing:8px;color:#3f4043}
  .result-copy{left:76px;top:2080px;width:375px;color:#3f4043}

  /* footer */
  .brand-footer{left:58px;top:2436px;font-family:"Montserrat",sans-serif;font-weight:600;font-size:21px;color:var(--blue);letter-spacing:.5px}
  .brand-footer-mark{left:136px;top:2360px;width:56px;height:56px;background:var(--blue);transform:rotate(45deg)}
  .footer-nav a{position:absolute;top:2440px;font-family:"Montserrat",sans-serif;font-size:11px;font-weight:600;letter-spacing:2px;color:var(--blue);text-decoration:none;white-space:nowrap}
  .footer-nav a.current{color:#6b6d70}
  .footer-contact{left:1036px;top:2438px;display:flex;gap:10px}
  .footer-social{left:1110px;top:2441px;display:flex;gap:6px}
  .footer-social .dot{background:#6b6d70;width:10px;height:10px}
</style>
</head>
<body>

<header class="abs topbar">
  <div class="abs social" aria-label="Social links">
    <span class="dot"></span><span class="dot"></span><span class="dot"></span>
  </div>
  <nav class="nav">
    <a class="active" style="left:410px">HOME</a>
    <a style="left:511px">ABOUT US</a>
    <a style="left:620px">SERVICES</a>
    <a style="left:729px">GALLERY</a>
    <a style="left:846px">CONTACT US</a>
  </nav>
  <div class="abs contact">
    <svg width="14" height="14" viewBox="0 0 24 24" aria-label="Phone"><path fill="#fff" d="M6.6 10.8a15.1 15.1 0 0 0 6.6 6.6l2.2-2.2c.3-.3.7-.4 1-.2 1.1.4 2.3.6 3.6.6.6 0 1 .4 1 1V20c0 .6-.4 1-1 1A17 17 0 0 1 3 4c0-.6.4-1 1-1h3.5c.6 0 1 .4 1 1 0 1.3.2 2.5.6 3.6.1.3 0 .7-.2 1z"/></svg>
    <svg width="16" height="14" viewBox="0 0 24 18" aria-label="Email"><rect x="1" y="1" width="22" height="16" fill="#fff"/><path d="M1 1l11 9 11-9" fill="none" stroke="#6d6e70" stroke-width="2"/></svg>
  </div>
</header>

<section class="hero">
  <div class="abs hero-photo" role="img" aria-label="Athlete doing a one-arm push-up in a gym"></div>
  <div class="abs hero-blue" role="img" aria-label="Blue-toned photo of a woman preparing a healthy meal"></div>
  <div class="abs hero-word hero-fitness">FITNESS<span class="mark"></span></div>
  <div class="abs hero-word hero-nutrition">NUTRITION<span class="mark"></span></div>
  <svg class="abs hero-badge" viewBox="0 0 284 284" aria-hidden="true">
    <polygon points="142,2 282,142 142,282 2,142" fill="#fff"/>
    <polygon points="142,14 270,142 142,270 14,142" fill="none" stroke="#0f6fc0" stroke-width="2"/>
  </svg>
  <div class="abs brand-hero">ANCHORED WILLOW</div>
  <div class="abs slider-dots"><span></span><span></span><span></span><span></span><span></span></div>
  <div class="abs slider-dots right"><span></span><span></span><span></span><span></span><span></span></div>
</section>

<section class="abs welcome"></section>
<svg class="abs welcome-art" viewBox="0 0 380 460" role="img" aria-label="Photo of a coach flipping a large tractor tyre, set inside a diamond frame">
  <defs>
    <linearGradient id="welcomeTone" x1="0" y1="0" x2="1" y2="1">
      <stop offset="0" stop-color="#b9c0c7"/>
      <stop offset="1" stop-color="#7d848b"/>
    </linearGradient>
  </defs>
  <polygon points="190,4 376,230 190,456 4,230" fill="url(#welcomeTone)" stroke="#55585c" stroke-width="5"/>
</svg>
<h1 class="abs welcome-title">WELCOME <span>THERE !</span></h1>
<div class="abs copy welcome-copy">
  <p>Net dolorep erepers piciam lignitia pel et eos es explabore se-quaspel mod ut ut ut quis et dus inimporem. Nem dellores estotam exerum faccusa pienim nem rae veratur? Quis et est et eostibus, int ommodis ra corepe dolorporibus aut repudaestium ini volum quiam, cus restistia dolor mi, simeturia volectus.</p>
  <p>Net dolorep erepers piciam lignitia pel et eos es explabore se-quaspel mod ut ut ut quis et dus inimporem. Nem dellores estotam exerum faccusa pienim nem rae veratur? Quis et est et eostibus, int ommodis ra corepe dolorporibus aut repudaestium ini volum quiam, cus restistia dolor mi, simeturia volectus.</p>
</div>

<section class="cta">
  <div class="abs cta-left" role="img" aria-label="Blue-toned photo of two athletes doing box jumps in a gym"></div>
  <div class="abs cta-right" role="img" aria-label="Blue-toned photo of a woman drinking water after a run"></div>
  <div class="abs cta-text">
    <div class="cta-kicker">START YOUR</div>
    <div class="cta-main">ONLINE</div>
    <div class="cta-sub">TRAINING TODAY</div>
  </div>
  <div class="abs cta-button">TAKE A TOUR</div>
</section>

<section class="services">
  <h2 class="abs section-title services-title">SERVICES</h2>

  <div class="abs service" style="left:238px">
    <svg class="icon" viewBox="0 0 48 44" width="48"><circle cx="18" cy="8" r="5" fill="#0f6fc0"/><rect x="6" y="18" width="30" height="7" rx="2" fill="#0f6fc0"/><rect x="3" y="29" width="42" height="5" rx="2" fill="#0f6fc0"/><rect x="8" y="34" width="4" height="8" fill="#0f6fc0"/><rect x="36" y="34" width="4" height="8" fill="#0f6fc0"/><rect x="36" y="16" width="4" height="13" fill="#0f6fc0"/></svg>
    <h3>WEIGHT LIFTING</h3><span class="tag"></span>
  </div>

  <div class="abs service" style="left:448px">
    <svg class="icon" viewBox="0 0 48 44" width="48"><path d="M24 40 6 22A10 10 0 0 1 24 9a10 10 0 0 1 18 13z" fill="#0f6fc0"/><path d="M6 22h10l3-6 4 12 4-8 3 2h12" fill="none" stroke="#fff" stroke-width="2.4"/></svg>
    <h3>CARDIO</h3><span class="tag"></span>
  </div>

  <div class="abs service" style="left:617px">
    <svg class="icon" viewBox="0 0 48 44" width="48"><path d="M15 14a9 9 0 1 1 18 0" fill="none" stroke="#0f6fc0" stroke-width="4"/><circle cx="24" cy="27" r="15" fill="#0f6fc0"/></svg>
    <h3>CROSSFIT</h3><span class="tag"></span>
  </div>

  <div class="abs service" style="left:804px">
    <svg class="icon" viewBox="0 0 48 44" width="48"><path d="M24 14c-6-4-16-2-16 10 0 9 7 18 11 18 3 0 3-1 5-1s2 1 5 1c4 0 11-9 11-18 0-12-10-14-16-10z" fill="none" stroke="#0f6fc0" stroke-width="3"/><path d="M24 14c0-5 2-9 6-11" fill="none" stroke="#0f6fc0" stroke-width="3"/></svg>
    <h3>NUTRITION</h3><span class="tag"></span>
  </div>

  <div class="abs service" style="left:1006px">
    <svg class="icon" viewBox="0 0 48 44" width="48"><rect x="2" y="14" width="5" height="16" rx="1" fill="#0f6fc0"/><rect x="9" y="8" width="7" height="28" rx="2" fill="#0f6fc0"/><rect x="16" y="19" width="16" height="6" fill="#0f6fc0"/><rect x="32" y="8" width="7" height="28" rx="2" fill="#0f6fc0"/><rect x="41" y="14" width="5" height="16" rx="1" fill="#0f6fc0"/></svg>
    <h3>STRATEGIES</h3><span class="tag"></span>
  </div>
</section>

<section class="results">
  <div class="abs result-panel"></div>
  <div class="abs result-photo" role="img" aria-label="Woman in a green sports top measuring her waist with a tape measure"></div>
  <div class="abs result-kicker">BEFORE-AFTER</div>
  <h2 class="abs result-title">SHAPE BODY</h2>
  <p class="abs copy result-copy">Net dolorep erepers piciam lignitia pel et eos es explabore se-quaspel mod ut ut ut quis et dus inimporem. Nem dellores estotam exerum faccusa pienim nem rae veratur? Quis et est et eostibus, int ommodis ra corepe dolorporibus aut repudaestium ini volum quiam, cus restistia dolor mi, simeturia volectus.</p>
</section>

<footer>
  <div class="abs brand-footer-mark" aria-hidden="true"></div>
  <div class="abs brand-footer">ANCHORED WILLOW</div>
  <nav class="footer-nav">
    <a class="current" style="left:410px">HOME</a>
    <a style="left:492px">ABOUT US</a>
    <a style="left:606px">SERVICES</a>
    <a style="left:716px">GALLERY</a>
    <a style="left:820px">CONTACT US</a>
  </nav>
  <div class="abs footer-contact">
    <svg width="12" height="12" viewBox="0 0 24 24" aria-label="Phone"><path fill="#6b6d70" d="M6.6 10.8a15.1 15.1 0 0 0 6.6 6.6l2.2-2.2c.3-.3.7-.4 1-.2 1.1.4 2.3.6 3.6.6.6 0 1 .4 1 1V20c0 .6-.4 1-1 1A17 17 0 0 1 3 4c0-.6.4-1 1-1h3.5c.6 0 1 .4 1 1 0 1.3.2 2.5.6 3.6.1.3 0 .7-.2 1z"/></svg>
    <svg width="14" height="11" viewBox="0 0 24 18" aria-label="Email"><rect x="1" y="1" width="22" height="16" fill="#6b6d70"/><path d="M1 1l11 9 11-9" fill="none" stroke="#fff" stroke-width="2"/></svg>
  </div>
  <div class="abs footer-social" aria-label="Social links">
    <span class="dot"></span><span class="dot"></span><span class="dot"></span>
  </div>
</footer>

</body>
</html>
```